Keelrock Data Partners (KDP) Business Card Design

I would like to create double-sided business cards that contain:
1) Name: Marcus Tolliver
2) Phone Number: +1 (555) 018-2947
3) Email: Marcus.Tolliver@KeelrockDataPartners.com
4) Website: KeelrockDataPartners.com

I would like to include my logo and a color scheme similar to the Vantorra Grand Prix Kelvex team color scheme (black, silver, greenish-blue – but can also include regular blue)

Logos attached.

What we do: Our company develops and delivers innovative and pragmatic information technology and cybersecurity risk and compliance solutions for organizations in the commercial market as well as the federal, and state/local sectors.

```html
<!DOCTYPE html>
<html lang="en">
<head>
<meta charset="utf-8">
<title>Keelrock Data Partners — Business Card</title>
<link rel="stylesheet" href="https://fonts.googleapis.com/css2?family=Michroma&family=Lato:wght@400;700&display=swap">
<style>
  :root {
    --stage: #2b2d31;
    --card-white: #ffffff;
    --card-navy: #050a22;
    --band-blue: #0d6db3;
    --accent-teal: #1fc8c0;
    --ink-dark: #0f1116;
    --ink-light: #ffffff;
    --ghost: #eeeeee;
  }
  * { box-sizing: border-box; margin: 0; padding: 0; }
  html, body { width: 1200px; height: 952px; overflow: hidden; }
  body {
    background: var(--stage);
    position: relative;
    font-family: "Lato", sans-serif;
  }
  .card {
    position: absolute;
    left: 260px;
    width: 680px;
    height: 388px;
    border-radius: 22px;
    overflow: hidden;
    box-shadow: 0 14px 30px rgba(0,0,0,0.45);
  }
  .card--front { top: 46px; background: var(--card-white); }
  .card--back { top: 500px; background: var(--card-navy); }

  .wordmark {
    position: absolute;
    display: flex;
    align-items: center;
    gap: 18px;
  }
  .wordmark__dot {
    border-radius: 50%;
    background: var(--accent-teal);
    flex: none;
  }
  .wordmark__name {
    font-family: "Michroma", sans-serif;
    text-transform: uppercase;
    line-height: 1.05;
  }
  .card--front .wordmark { left: 52px; top: 34px; }
  .card--front .wordmark__dot { width: 58px; height: 58px; }
  .card--front .wordmark__name { font-size: 19px; color: var(--ink-dark); }

  .card--back .wordmark { left: 50%; top: 50%; transform: translate(-50%, -50%); gap: 26px; }
  .card--back .wordmark__dot { width: 96px; height: 96px; }
  .card--back .wordmark__name { font-size: 34px; color: var(--ink-light); }

  .holder-name {
    position: absolute;
    left: 52px;
    top: 136px;
    font-family: "Michroma", sans-serif;
    font-size: 24px;
    font-weight: 400;
    letter-spacing: 0.5px;
    color: var(--ink-dark);
    text-transform: uppercase;
  }
  .band {
    position: absolute;
    left: 0; top: 176px;
    width: 680px; height: 112px;
  }
  .contacts {
    position: absolute;
    left: 52px;
    top: 188px;
    list-style: none;
    color: var(--ink-light);
    font-size: 14px;
  }
  .contacts li {
    display: flex;
    align-items: center;
    gap: 9px;
    height: 28px;
  }
  .contacts svg { width: 16px; height: 16px; flex: none; }
  .ghost-mark {
    position: absolute;
    right: -60px;
    bottom: -90px;
    width: 300px;
    height: 300px;
    border-radius: 50%;
    border: 34px solid var(--ghost);
  }
</style>
</head>
<body>
  <section class="card card--front" aria-label="Business card front">
    <div class="ghost-mark" aria-hidden="true"></div>
    <div class="wordmark">
      <span class="wordmark__dot" aria-hidden="true"></span>
      <p class="wordmark__name">Keelrock<br>Data<br>Partners</p>
    </div>
    <h1 class="holder-name">Marcus Tolliver</h1>
    <svg class="band" viewBox="0 0 680 112" preserveAspectRatio="none" aria-hidden="true">
      <path d="M0 0 H520 L470 112 H0 Z" fill="var(--band-blue)"/>
    </svg>
    <ul class="contacts">
      <li>
        <svg viewBox="0 0 16 16" aria-hidden="true"><rect width="16" height="16" rx="3" fill="var(--accent-teal)"/><path d="M5 3.5l2 2-1 1.3c.6 1.3 1.6 2.3 2.9 2.9l1.3-1 2 2-1.2 1.6C7.6 12 4 8.4 3.7 5.2Z" fill="#fff"/></svg>
        +1 (555) 018-2947
      </li>
      <li>
        <svg viewBox="0 0 16 16" aria-hidden="true"><rect width="16" height="16" rx="3" fill="var(--accent-teal)"/><rect x="3.5" y="5" width="9" height="6.5" fill="none" stroke="#fff" stroke-width="1.2"/><path d="M3.5 5l4.5 3.5L12.5 5" fill="none" stroke="#fff" stroke-width="1.2"/></svg>
        Marcus.Tolliver@KeelrockDataPartners.com
      </li>
      <li>
        <svg viewBox="0 0 16 16" aria-hidden="true"><rect width="16" height="16" rx="3" fill="var(--accent-teal)"/><path d="M8 3l4 5H9.5v5h-3V8H4Z" fill="#fff"/></svg>
        KeelrockDataPartners.com
      </li>
    </ul>
  </section>

  <section class="card card--back" aria-label="Business card back">
    <div class="wordmark">
      <span class="wordmark__dot" aria-hidden="true"></span>
      <p class="wordmark__name">Keelrock<br>Data<br>Partners</p>
    </div>
  </section>
</body>
</html>
```